Refer a Friend A5 Flyer for Healthcare Staff

We need an A5 flyer that we can hand out to existing and new staff members promoting our Refer a friend Scheme. We need the leaflet to encourage staff to talk to their family and friends about joining our Healthcare Agency, which provides staff to local care related establishments. Using our logo and brand colours blue and green, as per our website, the final design will need to clearly convey the benefits and attractions of referring additional staff to the team. In addition is the promotion of our Friendhub page, requesting staff to like the page and to like and share various posts.

Target Market(s)

Healthcare and potential Healthcare Staff

Industry/Entity Type

Healthcare

Colors
33b8a4
3277b5

Requirements
Must have
• Company Logo, Brand colours,
• text; "Refer a Friend and receive a £50 Bonus after just 1 completed shift"
• text; "3 easy steps to refer a friend, 1 Fill out your name on the back of your Business Card 2 Hand the card to your friend or any person you wish to refer, 3 ask your friend to present the card to us when they attend their interview"
• text; "Like and share any of our Open Days on Friendhub for a chance to win a prize, you can find us easily by searching @CarewellPlacementGroup"
• text; "Like our Page to stay up to date with our events and offers"
Nice to have
• care worker / elderly care / support worker pictures
• Content / pics from website www.carewellplacementgroup.co.uk

```html
<!DOCTYPE html>
<html lang="en">
<head>
<meta charset="utf-8">
<title>Refer a Friend Flyer – Carewell Placement Group</title>
<link href="https://fonts.googleapis.com/css2?family=Kaushan+Script&family=Lilita+One&family=Open+Sans:wght@400;600;700&display=swap" rel="stylesheet">
<style>
  :root {
    --green-deep: #0f8f6c;
    --green-mid: #1ea47e;
    --green-bright: #33b8a4;
    --green-soft: #5cc9a5;
    --brand-blue: #3277b5;
    --sun-yellow: #f6d23a;
    --ink-dark: #143a33;
    --white: #ffffff;
  }
  * { box-sizing: border-box; margin: 0; padding: 0; }
  html, body { width: 1200px; height: 829px; overflow: hidden; background: #ffffff; }
  .flyer {
    position: relative;
    width: 1200px;
    height: 829px;
    overflow: hidden;
    font-family: "Open Sans", Arial, sans-serif;
    background: linear-gradient(100deg, var(--green-deep) 0%, var(--green-mid) 35%, var(--green-bright) 60%, var(--green-soft) 100%);
  }
  .photo-area {
    position: absolute;
    top: 0; right: 0;
    width: 560px; height: 829px;
    background:
      radial-gradient(ellipse at 40% 28%, #efd8c6 0%, rgba(239,216,198,0) 36%),
      radial-gradient(ellipse at 72% 42%, #f4ece4 0%, rgba(244,236,228,0) 40%),
      linear-gradient(180deg, #d7e6e0 0%, #7fcfb2 55%, #2fae86 100%);
  }
  .photo-fade {
    position: absolute;
    top: 0; left: 620px;
    width: 240px; height: 829px;
    background: linear-gradient(90deg, rgba(40,176,136,1) 0%, rgba(40,176,136,0.8) 45%, rgba(40,176,136,0) 100%);
  }
  .swoops { position: absolute; inset: 0; }
  .brand {
    position: absolute;
    left: 50px; top: 62px;
    display: flex; align-items: center; gap: 14px;
  }
  .brand-mark {
    width: 30px; height: 30px; border-radius: 50%;
    background: var(--brand-blue);
    flex: none;
  }
  .brand-name {
    font-weight: 700;
    font-size: 32px;
    line-height: 1.08;
    color: var(--brand-blue);
  }
  .offer {
    position: absolute;
    left: 40px; top: 296px;
    width: 330px;
    color: var(--white);
  }
  .offer-title {
    font-family: "Kaushan Script", cursive;
    font-size: 50px;
    line-height: 1;
    color: var(--sun-yellow);
    padding-left: 6px;
  }
  .offer-row { display: flex; align-items: center; gap: 18px; height: 76px; }
  .megaphone-icon {
    width: 70px; height: 70px; border-radius: 50%;
    background: radial-gradient(circle, #f4f4f4 0%, #d9d9d9 70%);
    flex: none;
  }
  .offer-friend {
    font-family: "Kaushan Script", cursive;
    font-size: 38px;
    line-height: 1;
    color: var(--sun-yellow);
    transform: translateY(-10px);
  }
  .offer-receive {
    font-family: "Kaushan Script", cursive;
    font-size: 34px;
    line-height: 1.1;
  }
  .offer-amount {
    font-family: "Lilita One", sans-serif;
    font-size: 108px;
    line-height: 0.95;
    color: var(--sun-yellow);
    letter-spacing: 2px;
  }
  .offer-bonus {
    font-family: "Lilita One", sans-serif;
    font-size: 92px;
    line-height: 0.95;
    color: var(--sun-yellow);
  }
  .offer-note {
    font-size: 26px;
    font-weight: 600;
    line-height: 1.15;
    margin-top: 6px;
  }
  .divider {
    position: absolute;
    left: 386px; top: 290px;
    width: 2px; height: 462px;
    background: rgba(255,255,255,0.85);
  }
  .steps {
    position: absolute;
    left: 432px; top: 212px;
    width: 380px;
  }
  .steps-title {
    font-family: "Kaushan Script", cursive;
    font-size: 54px;
    line-height: 1;
    color: var(--white);
  }
  .steps-sub {
    font-size: 22px;
    color: var(--white);
    margin-top: 2px;
  }
  .steps-list { list-style: none; margin-top: 10px; }
  .step {
    display: flex; align-items: center; gap: 26px;
    height: 146px;
    padding-left: 10px;
    border-bottom: 2px solid rgba(255,255,255,0.6);
  }
  .step:last-child { border-bottom: none; }
  .step-number {
    font-family: "Lilita One", sans-serif;
    font-size: 94px;
    line-height: 1;
    color: var(--sun-yellow);
    width: 48px;
    flex: none;
  }
  .step-text {
    font-size: 21px;
    line-height: 1.3;
    color: var(--ink-dark);
    font-weight: 600;
  }
  .social-line {
    position: absolute;
    left: 42px; bottom: 10px;
    display: flex; align-items: center; gap: 14px;
    color: var(--white);
  }
  .social-dot {
    width: 36px; height: 36px; border-radius: 50%;
    border: 2px solid var(--white);
    flex: none;
  }
  .social-main { font-size: 17px; line-height: 1.3; }
  .social-extra { font-size: 13px; line-height: 1.3; opacity: 0.95; }
</style>
</head>
<body>
<main class="flyer">
  <div class="photo-area" role="img" aria-label="Photo of a smiling care worker hugging an elderly woman seated in a wheelchair"></div>
  <div class="photo-fade"></div>

  <svg class="swoops" width="1200" height="829" viewBox="0 0 1200 829" aria-hidden="true">
    <path d="M0 0 H980 C760 40 560 140 420 210 C280 270 120 280 0 262 Z" fill="#1aa47d"/>
    <path d="M0 0 H900 C700 30 520 110 390 170 C250 230 110 240 0 226 Z" fill="#2bb98f"/>
    <path d="M0 0 H820 C640 20 480 80 360 140 C230 200 100 212 0 200 Z" fill="#ffffff"/>
  </svg>

  <div class="brand">
    <span class="brand-mark"></span>
    <span class="brand-name">Carewell<br>Placement Group</span>
  </div>

  <section class="offer">
    <p class="offer-title">Refer a</p>
    <div class="offer-row">
      <span class="megaphone-icon" role="img" aria-label="Megaphone illustration"></span>
      <span class="offer-friend">Friend</span>
    </div>
    <p class="offer-receive">&amp; receive a</p>
    <p class="offer-amount">£50</p>
    <p class="offer-bonus">Bonus</p>
    <p class="offer-note">after just one<br>completed shift</p>
  </section>

  <div class="divider"></div>

  <section class="steps">
    <h2 class="steps-title">Three</h2>
    <p class="steps-sub">easy steps to refer a friend</p>
    <ol class="steps-list">
      <li class="step"><span class="step-number">1</span><span class="step-text">Fill out your name<br>on the back of your<br>Business Card</span></li>
      <li class="step"><span class="step-number">2</span><span class="step-text">Hand the card to<br>your friend or any<br>person you wish to refer</span></li>
      <li class="step"><span class="step-number">3</span><span class="step-text">Ask your friend to present<br>the card to us when<br>they attend their interview</span></li>
    </ol>
  </section>

  <footer class="social-line">
    <span class="social-dot"></span>
    <div>
      <p class="social-main">Like and share any of our Open Days on Friendhub for a chance to win a prize</p>
      <p class="social-extra">Find us by searching @CarewellPlacementGroup · Like our Page to stay up to date with our events and offers</p>
    </div>
  </footer>
</main>
</body>
</html>
```